15 ft high by 10 ft wide road side sign

road side sign - this is a dual carrigeway speeds of 40 mph so eye time to see ,read and absorb very short is less than 3 seconds 45,000 vehicles a day go past these are local to us our most profitable business is customers instore we embroider company and club and school logos and badges one mile ahead of this sign we have over 400,000 logos we have sewn and are on our servers we are well know in our area we can sew your logo in under 2 hours if it is already on our server we have a fast track service which we charge extra for very profitable is the customers buying items on vortiq and shopnu we can really be fast on your own items if you bring them instore we have 15 large multi head machine to cope no one else is that fast on line embroidery takes 7 -10 days we have purchased from others saying 24 hours when put to the test they fail and give excusses why it cannot be do every time we have brought and our customers say the same project your logo embrodery one mile ahead ------- road side sign 15 ft high 10 feet wide company name Swift Thread & Stitchworks 12 Harrowgate Close KT7 4PD like drivers to be able to drop off and collect sameday because driving you have very very little time to read has to be simple good thing is its a major commutor route A10 Enfield so drivers can be trained via repeat reading dale finch

Target Market(s)

our local area is our most profitable market getting people instore online is to slow to for our custopmers and low a margin for us 1,000,000 people withing 2 miles of our store

Industry/Entity Type

Embroidery

Font styles to use
Sans Serif

Colors

Designer to choose colors to be used in the design.

Requirements
Must have
• simple easy to read
• also
• nigel parsons lovers he has NP sewn on his union jack boxer shorts
• as clothing with your company logo are 100% tax deductable for most companies
• as promotional wear
Should not have
• to complicated to read and understand so many people driving past are not english readers as there main language

```html
<!DOCTYPE html>
<html lang="en">
<head>
<meta charset="utf-8">
<title>Swift Thread &amp; Stitchworks – Roadside Sign</title>
<link href="https://fonts.googleapis.com/css2?family=Roboto:wght@500;700;900&display=swap" rel="stylesheet">
<style>
  :root {
    --page-bg: #d9d9d9;
    --sign-top: #ffffff;
    --sign-bottom: #e9e9e9;
    --brand-red: #d0202a;
    --brand-navy: #2b2a7e;
    --ink: #1e1e1e;
    --url-bar: #4a4a4a;
    --white: #ffffff;
  }
  * { margin: 0; padding: 0; box-sizing: border-box; }
  html, body {
    width: 768px;
    height: 1200px;
    overflow: hidden;
    background: var(--page-bg);
    font-family: "Roboto", Arial, sans-serif;
  }
  .sign {
    position: absolute;
    left: 124px;
    top: 210px;
    width: 520px;
    height: 780px;
    background: linear-gradient(160deg, var(--sign-top) 0%, #f4f4f4 55%, var(--sign-bottom) 100%);
    box-shadow: 0 4px 14px rgba(0, 0, 0, 0.35);
    overflow: hidden;
  }
  .brand-name {
    position: absolute;
    left: 40px;
    top: 38px;
    display: flex;
    align-items: center;
    gap: 12px;
    color: var(--brand-navy);
    font-weight: 900;
    font-size: 26px;
    line-height: 1.05;
    text-transform: uppercase;
  }
  .brand-name .brand-mark {
    width: 22px;
    height: 22px;
    background: var(--brand-red);
    flex: none;
  }
  .headline {
    position: absolute;
    left: 38px;
    top: 128px;
    font-weight: 700;
    font-size: 56px;
    line-height: 58px;
    letter-spacing: -0.5px;
  }
  .headline .line-red { color: var(--brand-red); display: block; }
  .headline .line-navy { color: var(--brand-navy); display: block; }
  .tagline {
    position: absolute;
    left: 40px;
    top: 256px;
    color: var(--ink);
    font-weight: 500;
    font-size: 26px;
  }
  .fast-track {
    position: absolute;
    left: 40px;
    top: 312px;
    width: 440px;
    background: var(--brand-navy);
    color: var(--white);
    padding: 12px 18px;
    font-weight: 700;
    text-transform: uppercase;
  }
  .fast-track .service { display: block; font-size: 25px; line-height: 32px; }
  .fast-track .distance {
    display: flex;
    align-items: center;
    gap: 10px;
    font-size: 25px;
    line-height: 32px;
    color: #ffd9db;
  }
  .fast-track .distance svg { width: 30px; height: 22px; flex: none; }
  .models-photo {
    position: absolute;
    left: 0;
    top: 440px;
    width: 290px;
    height: 340px;
    background: linear-gradient(90deg, #f36a2c 0%, #ef5a30 38%, #d9252f 62%, #c81f2a 100%);
    border-radius: 120px 120px 0 0;
  }
  .garments-photo {
    position: absolute;
    left: 304px;
    top: 540px;
    width: 216px;
    height: 188px;
    background: linear-gradient(90deg, #1f63d6 0%, #2a6fe0 60%, #9be04a 78%, #b5ee3a 100%);
    border-radius: 44px 14px 0 0;
  }
  .url-bar {
    position: absolute;
    left: 276px;
    top: 728px;
    width: 244px;
    height: 52px;
    background: var(--url-bar);
    color: var(--white);
    font-weight: 700;
    font-size: 17px;
    display: flex;
    align-items: center;
    justify-content: center;
  }
</style>
</head>
<body>
  <main class="sign">
    <div class="brand-name">
      <span class="brand-mark"></span>
      <span>Swift Thread<br>&amp; Stitchworks</span>
    </div>

    <h1 class="headline">
      <span class="line-red">SWEATSHIRTS</span>
      <span class="line-navy">&amp; HOODIES</span>
    </h1>

    <p class="tagline">We Embroider YOUR Clothing</p>

    <p class="fast-track">
      <span class="service">Same Day Logo Embroidery</span>
      <span class="distance">
        <svg viewBox="0 0 30 22" aria-hidden="true"><path d="M2 11h22M16 3l8 8-8 8" fill="none" stroke="currentColor" stroke-width="4" stroke-linecap="round" stroke-linejoin="round"/></svg>
        1 Mile Ahead
      </span>
    </p>

    <div class="models-photo" role="img" aria-label="Photo of a man in an orange t-shirt and a woman in a red polo shirt"></div>
    <div class="garments-photo" role="img" aria-label="Photo of a royal blue sweatshirt and a yellow hi-vis vest"></div>

    <div class="url-bar">www.swiftthread.co.uk</div>
  </main>
</body>
</html>
```